Business card design for a debt inventory management software company

We need a business card design to help us move into the next phase of our business. We developed an innovative solution to help companies collect their bad debts. We are moving into a new era and branching out into new industries. We are open to design ideas but would like that they have a similar feel/look to our website and include our logo. https://www.ledgorvia.com

Target Market(s)

Finance Industry, Telecom Industry, Utility Industry, Healthcare Industry, Insurance Industry

Industry/Entity Type

Software

Contact Information for Business Card

Include Name, Title, Phone, Email, website, address, and logo

Font styles to use
Sans Serif

Colors

Designer to choose colors to be used in the design.

Requirements
Must have
• A similar look and feel to our website. https://www.ledgorvia.com

```html
<!DOCTYPE html>
<html lang="en">
<head>
<meta charset="utf-8">
<title>Ledgorvia Software – Business Card</title>
<link href="https://fonts.googleapis.com/css2?family=Raleway:wght@300;400;500;700&display=swap" rel="stylesheet">
<style>
  :root {
    --brand-blue: #263a87;
    --ink-blue: #2b3f8f;
    --accent-yellow: #f2bd2a;
    --text-grey: #4a4a4a;
    --stage: #d3d3d3;
    --card-white: #ffffff;
  }
  * { box-sizing: border-box; margin: 0; padding: 0; }
  html, body {
    width: 1200px; height: 930px; overflow: hidden;
    background: var(--stage);
    font-family: "Raleway", sans-serif;
  }
  .card {
    position: absolute;
    width: 620px; height: 354px;
    border-radius: 26px;
    overflow: hidden;
    box-shadow: 0 6px 14px rgba(0,0,0,0.25);
  }
  .card--front { left: 290px; top: 70px; background: var(--brand-blue); }
  .card--back  { left: 290px; top: 490px; background: var(--card-white); }

  .front-wordmark {
    position: absolute; left: 0; right: 0; top: 140px;
    text-align: center;
    color: #fff; font-weight: 300; font-size: 44px; letter-spacing: 0.5px;
  }

  .back-brand {
    position: absolute; left: 44px; top: 180px;
    display: flex; align-items: center; gap: 12px;
    white-space: nowrap;
  }
  .back-brand__mark { width: 22px; height: 22px; background: var(--brand-blue); flex: none; }
  .back-brand__name { color: var(--brand-blue); font-weight: 300; font-size: 26px; }

  .divider {
    position: absolute; left: 354px; top: 44px;
    width: 1.5px; height: 196px; background: var(--ink-blue);
  }

  .contact { position: absolute; left: 376px; top: 40px; right: 16px; color: var(--text-grey); white-space: nowrap; }
  .contact__name { color: var(--ink-blue); font-weight: 700; font-size: 21px; letter-spacing: 0.4px; }
  .contact__title { font-size: 15px; margin-bottom: 10px; }
  .contact__list { list-style: none; font-size: 14px; line-height: 21px; }
  .contact__list li { display: flex; align-items: center; gap: 8px; }
  .contact__list svg { width: 10px; height: 10px; fill: var(--ink-blue); flex: none; }
  .contact__list strong { color: var(--ink-blue); font-weight: 500; }
  .contact__address { font-size: 14px; line-height: 19px; margin-top: 8px; }

  .swoosh { position: absolute; left: 0; bottom: 0; width: 620px; height: 354px; }
</style>
</head>
<body>

  <section class="card card--front" aria-label="Card front">
    <p class="front-wordmark">Ledgorvia Software</p>
  </section>

  <section class="card card--back" aria-label="Card back">
    <div class="back-brand">
      <span class="back-brand__mark"></span>
      <span class="back-brand__name">Ledgorvia Software</span>
    </div>

    <div class="divider"></div>

    <div class="contact">
      <h1 class="contact__name">DARREN HOLLOWAY</h1>
      <p class="contact__title">Director</p>
      <ul class="contact__list">
        <li><svg viewBox="0 0 10 10"><path d="M2 0h2l1 3-1.5 1a6 6 0 0 0 2.5 2.5L7 5l3 1v2a2 2 0 0 1-2 2A8 8 0 0 1 0 2a2 2 0 0 1 2-2z"/></svg><span>555.210.0400</span></li>
        <li><svg viewBox="0 0 10 10"><rect x="2" y="0" width="6" height="10" rx="1.2"/></svg><span>555.318.5501</span></li>
        <li><svg viewBox="0 0 10 10"><path d="M0 2h10v6H0z M0 2l5 3.5L10 2" fill="none" stroke="#2b3f8f" stroke-width="1.2"/></svg><span>info@ledgorvia.com</span></li>
        <li><svg viewBox="0 0 10 10"><circle cx="5" cy="5" r="4.4" fill="none" stroke="#2b3f8f" stroke-width="1.2"/><path d="M0.6 5h8.8M5 0.6v8.8" stroke="#2b3f8f" stroke-width="1"/></svg><span>www.<strong>ledgorvia</strong>.com</span></li>
      </ul>
      <p class="contact__address">48 Brennan Park Road,<br>Suite 210, Hartwell, Ohio 44990</p>
    </div>

    <svg class="swoosh" viewBox="0 0 620 354" aria-hidden="true">
      <path d="M0 354 L0 344 L440 330 C462 329 466 304 492 300 L620 296 L620 354 Z" fill="var(--brand-blue)"/>
      <path d="M0 339 L432 325" stroke="var(--accent-yellow)" stroke-width="5" fill="none"/>
    </svg>
  </section>

</body>
</html>
```